Digital Marketing Agency Needs a Pagecraft Web Design

We need a web design for a new company based in Evergreen, Colorado (the greater Denver Metro area) called "Copper Wayfarer". We are a full service Digital Marketing Agency that offers and provides the following services to clients: Website Design, Search Engine Optimization, Plexo Local Listing, Local Online Directories, Reputation Marketing, Social Media Marketing, Video Marketing, Pay Per Click. Our slogan is "Digital Marketing, Elevated!" We want a PageCraft web design that has a very modern look. We would like to see designs use the following colors (included color code):

light blue (#0cb9ea)
orange (#f47528)
white (#ffffff)
black (#000000).

These colors coincide with the colors of our logo (attached). We prefer a flat design but would like some elements of depth. We need a header that includes a logo (attached), name/address/phone number of our company, a contact call-to-action button (these need to be very easy to locate on the page), menu bar, and banner (very flexible to set up of banner).. The footer needs to include logo, NAP, Footer Menu, Section for blogs (includes title of blog that links to post), & copyright. We also need a way to prominently display and link our key featured services (Website Design, Search Engine Optimization, Plexo Local Listing, Local Online Directories, Reputation Marketing, Social Media Marketing, Video Marketing, Pay Per Click).

Here are three websites that we really like and would like to see certain elements incorporated:

1. http://quillstonemedia.example/ (like how the services were laid out on the home page for services -- "Features" section... want to follow this same type of idea, just in our own way).
2. http://tavenmark.example/ (love the modern, visual aspect of this site and how professionally clean it is.... very easy to understand and navigate through).
3. http://norvacreative.example/ (like how this site incorporates interactive features that engage people while visiting the site).

The overall goal of the site is to effectively emphasize the services we provide (see above), who we are, and how to contact us for services.

** Any stock photos used HAVE TO BE TAKEN from Lumafold Pictures (http://www.lumafoldpics.example/). And if watermarked, please provide the image code for each image used.

Target Market(s)

Lawyers, Insurance agents, Real Estate, Restaurant Owners, Doctors and all other medical providers.

Industry/Entity Type

Internet

Number of Pages Required

1 page

Font styles to use
Serif

Colors
33a6d7
ffffff
000000
f37122

Requirements
Must have
• 1. Header w/ Logo, Name/Address/Phone Number of our business, a call-to-action button to "Contact us":
• Copper Wayfarer – Digital Marketing
• 41872 Cobblewick Drive
• Evergreen, CO 80439
• 303-547-9183
• 2. Navigation Menu
• 3. Some type of banner
• 4. Featured Services section (with a short blurb about each)
• 5. Contact Form (somewhere above the fold)
• 6. Need at least 2-3 paragraphs of text (use dummy text) somewhere on the page (either in full or in sections)....
• 7. Footer that includes logo, NAP (see above), Menu Links, Links for services (see above), Blog Section, Social Media icons (Chatterly, Peepline, Plexo+, and ReelHub) & a copyright.
Nice to have
• Here are three websites that we really like and would be nice to see elements of incorporated:
• 1. http://quillstonemedia.example/ (like how the services were laid out on the home page -- "Features" section... want to follow this same type of idea, just in our own way).
• 2. http://tavenmark.example/ (love the modern, visual aspect of this site and how professionally clean it is.... very easy to understand and navigate through).
• 3. http://norvacreative.example/ (like how this site incorporates interactive features that engage people that visit the site).
Should not have
• Pretty flexible... We just need to make sure it's a Pagecraft web design.

```html
<!DOCTYPE html>
<html lang="en">
<head>
<meta charset="utf-8">
<title>Copper Wayfarer – Digital Marketing</title>
<link href="https://fonts.googleapis.com/css2?family=Open+Sans:wght@300;400;600;700&family=Oswald:wght@300;400&display=swap" rel="stylesheet">
<style>
:root{
  --blue:#0cb9ea;
  --orange:#f47528;
  --white:#ffffff;
  --black:#000000;
  --ink:#333333;
  --muted:#777777;
  --line:#dddddd;
  --footer:#1e1e1e;
  --footer-deep:#141414;
}
*{box-sizing:border-box;margin:0;padding:0}
html,body{width:1200px;height:2208px;overflow:hidden;background:var(--white)}
body{font-family:"Open Sans",sans-serif;color:var(--ink);position:relative}
.topbar{height:28px;background:#f4f4f4;border-bottom:1px solid var(--line);display:flex;align-items:center;padding:0 150px;font-size:11px;color:var(--muted);gap:26px}
.topbar span{display:flex;align-items:center;gap:6px}
.header{height:46px;display:flex;align-items:center;justify-content:space-between;padding:0 150px}
.brand{display:flex;align-items:center;gap:8px}
.brand-dot{width:22px;height:22px;border-radius:50%;background:var(--orange)}
.brand-name{font-size:22px;font-weight:700;color:var(--blue)}
.nav{display:flex;font-size:11px;font-weight:600}
.nav a{padding:8px 13px;color:var(--ink);text-decoration:none}
.nav a.active{background:var(--orange);color:var(--white)}
.hero{position:relative;height:328px;background:linear-gradient(120deg,#3c4650,#7a7468 45%,#2c3238);display:flex;flex-direction:column;align-items:center;justify-content:center;color:var(--white);text-align:center}
.hero h1{font-family:"Oswald",sans-serif;font-weight:300;font-size:40px;letter-spacing:2px}
.hero p{font-size:13px;letter-spacing:1px;margin-top:4px}
.btn{display:inline-block;background:var(--orange);color:var(--white);font-size:11px;font-weight:600;padding:8px 16px;margin-top:16px}
.hero .arrow{position:absolute;top:150px;width:30px;height:30px}
.hero .mouse{margin-top:34px}
.band{height:48px;background:var(--blue);color:var(--white);display:flex;align-items:center;justify-content:center;font-size:15px;letter-spacing:1px}
.band b{margin-left:6px}
.section-title{display:flex;align-items:center;justify-content:center;gap:16px;font-family:"Oswald",sans-serif;font-size:24px;color:var(--ink);letter-spacing:1px}
.section-title::before,.section-title::after{content:"";width:70px;height:2px;background:var(--orange)}
.services{position:relative;margin-top:32px}
.service-row{display:flex;margin-top:24px}
.service{width:200px;text-align:center}
.service .shot{height:330px;position:relative}
.service .label{font-size:12px;font-weight:600;margin-top:14px;color:var(--ink)}
.service .more{position:absolute;left:40px;top:145px;border:1px solid var(--white);color:var(--white);font-size:11px;font-weight:600;padding:6px 14px}
.side-arrow{position:absolute;top:225px;width:26px;height:40px;background:var(--orange);display:flex;align-items:center;justify-content:center}
.welcome{display:flex;gap:40px;padding:0 80px;margin-top:40px}
.welcome .shot{width:480px;height:300px;background:linear-gradient(135deg,#d7dbe0,#9aa6b2 60%,#6b7580)}
.welcome .copy{width:520px;padding-top:6px}
.welcome h2{font-size:20px;font-weight:600;color:var(--ink)}
.welcome h2 + .rule{width:50px;height:2px;background:var(--orange);margin:8px 0 10px}
.welcome p{font-size:11px;line-height:1.6;color:var(--muted);margin-bottom:10px}
.welcome p.lead{color:var(--ink);font-weight:600}
.blog{margin-top:42px}
.blog-row{display:flex;justify-content:center;gap:48px;margin-top:24px}
.post{width:430px;height:190px;display:flex;background:#f6f6f6;border:1px solid var(--line)}
.post .shot{width:220px;position:relative;background:linear-gradient(135deg,#c9ccd2,#7e8996)}
.post .date{position:absolute;left:0;right:0;bottom:0;height:26px;background:var(--orange);color:var(--white);font-size:12px;font-weight:700;display:flex;align-items:center;justify-content:center}
.post .text{padding:14px;width:210px}
.post h3{font-size:13px;font-weight:600;margin-bottom:6px}
.post p{font-size:10px;line-height:1.6;color:var(--muted)}
.post a{display:inline-block;margin-top:8px;font-size:10px;color:var(--orange);font-weight:600}
.contact{margin-top:22px;text-align:center}
.contact .sub{font-size:10px;color:var(--muted);margin-top:6px}
.form{display:flex;gap:16px;width:896px;margin:18px auto 0;text-align:left}
.fields{width:280px;display:flex;flex-direction:column;gap:10px}
.field{height:40px;border:1px solid var(--line);font-size:10px;color:var(--muted);padding:12px}
.message{flex:1;height:140px;border:1px solid var(--line);font-size:10px;color:var(--muted);padding:12px}
.send{background:var(--blue);margin-top:18px}
.footer{position:absolute;left:0;top:1880px;width:1200px;height:292px;background:var(--footer);color:#aaaaaa;display:flex;gap:40px;padding:26px 140px 0}
.footer .col{width:210px;font-size:10px;line-height:1.7}
.footer h4{color:var(--white);font-size:12px;font-weight:600;margin-bottom:4px}
.footer h4 + .rule{width:36px;height:2px;background:var(--orange);margin-bottom:10px}
.footer li{list-style:none;display:flex;gap:6px;align-items:center}
.footer li::before{content:"";width:4px;height:4px;background:var(--orange)}
.footer .brand{margin-bottom:10px}
.footer .brand-name{font-size:19px}
.socials{display:flex;gap:8px;margin-top:12px}
.socials span{width:22px;height:22px;border-radius:50%;background:#3a3a3a}
.copyright{position:absolute;left:0;top:2172px;width:1200px;height:36px;background:var(--footer-deep);color:#888888;font-size:10px;display:flex;align-items:center;justify-content:center}
</style>
</head>
<body>
<div class="topbar">
  <span><svg width="10" height="12" viewBox="0 0 10 12"><path d="M5 0a4 4 0 0 0-4 4c0 3 4 8 4 8s4-5 4-8a4 4 0 0 0-4-4z" fill="#f47528"/></svg>41872 Cobblewick Drive, Evergreen, CO 80439</span>
  <span><svg width="11" height="11" viewBox="0 0 11 11"><path d="M2 0l2 2.5-1 1.5a7 7 0 0 0 4 4l1.5-1L11 9l-1.5 2C5 11 0 6 0 1.5z" fill="#f47528"/></svg>303-547-9183</span>
</div>
<header class="header">
  <div class="brand"><span class="brand-dot"></span><span class="brand-name">Copper Wayfarer</span></div>
  <nav class="nav"><a class="active">HOME</a><a>ABOUT US</a><a>SERVICES</a><a>BLOGS</a><a>CONTACT US</a></nav>
</header>
<section class="hero" role="img" aria-label="Banner photo of a smiling woman working at an office desk">
  <svg class="arrow" style="left:20px" viewBox="0 0 30 30"><path d="M19 6l-9 9 9 9" stroke="#fff" stroke-width="2" fill="none"/></svg>
  <svg class="arrow" style="right:20px" viewBox="0 0 30 30"><path d="M11 6l9 9-9 9" stroke="#fff" stroke-width="2" fill="none"/></svg>
  <h1>LOREM IPSUM IS SIMPLY DUMMY TEXT</h1>
  <p>CONTRARY TO POPULAR BELIEF, LOREM IPSUM IS NOT SIMPLY RANDOM TEXT</p>
  <span class="btn">READ MORE</span>
  <svg class="mouse" width="16" height="24" viewBox="0 0 16 24"><rect x="1" y="1" width="14" height="22" rx="7" stroke="#fff" stroke-width="1.5" fill="none"/><line x1="8" y1="5" x2="8" y2="9" stroke="#fff" stroke-width="1.5"/></svg>
</section>
<div class="band">NEQUE PORRO QUISQUAM EST QUI DOLOREM IPSUM <b>QUIA DOLOR SIT AMET</b></div>

<section class="services">
  <h2 class="section-title">SERVICES WE PROVIDE</h2>
  <div class="service-row">
    <div class="service"><div class="shot" role="img" aria-label="Photo of a laptop showing a website layout" style="background:linear-gradient(160deg,#5e6f80,#2d3a46)"><span class="more">READ MORE</span></div><div class="label">WEBSITE DESIGN</div></div>
    <div class="service"><div class="shot" role="img" aria-label="Photo of search optimization sketches on paper" style="background:linear-gradient(160deg,#e4d9c4,#b69a6d)"></div><div class="label">SEARCH ENGINE OPTIMIZATION</div></div>
    <div class="service"><div class="shot" role="img" aria-label="Photo of a hand touching business icons" style="background:linear-gradient(160deg,#cfd7de,#7f93a5)"></div><div class="label">PLEXO LOCAL LISTING</div></div>
    <div class="service"><div class="shot" role="img" aria-label="Photo of a business meeting around a table" style="background:linear-gradient(160deg,#8f8a82,#45423e)"></div><div class="label">LOCAL ONLINE DIRECTORIES</div></div>
    <div class="service"><div class="shot" role="img" aria-label="Photo of people using a tablet" style="background:linear-gradient(160deg,#a9a094,#5d564d)"></div><div class="label">SOCIAL MEDIA MARKETING</div></div>
    <div class="service"><div class="shot" role="img" aria-label="Photo of a hand pointing at rating stars" style="background:linear-gradient(160deg,#dfe3e8,#8a95a0)"></div><div class="label">REPUTATION MARKETING</div></div>
  </div>
  <span class="side-arrow" style="left:0"><svg width="10" height="14" viewBox="0 0 10 14"><path d="M8 1L2 7l6 6" stroke="#fff" stroke-width="2" fill="none"/></svg></span>
  <span class="side-arrow" style="right:0"><svg width="10" height="14" viewBox="0 0 10 14"><path d="M2 1l6 6-6 6" stroke="#fff" stroke-width="2" fill="none"/></svg></span>
</section>

<section class="welcome">
  <div class="shot" role="img" aria-label="Photo of a smiling man working on a laptop"></div>
  <div class="copy">
    <h2>WELCOME TO COPPERWAYFARER.EXAMPLE</h2>
    <div class="rule"></div>
    <p class="lead">Lorem ipsum dolor sit amet, consectetur adipiscing elit, sed do eiusmod tempor incididunt ut labore.</p>
    <p>Lorem ipsum is simply dummy text of the printing and typesetting industry. Lorem ipsum has been the industry's standard dummy text ever since the 1500s, when an unknown printer took a galley of type and scrambled it to make a type specimen book. It has survived not only five centuries but also the leap into electronic typesetting.</p>
    <p>It was popularised in the 1960s with the release of sheets containing passages, and more recently with desktop publishing software including versions of lorem ipsum. Contrary to popular belief, it is not simply random text. It has roots in a piece of classical literature, making it over two thousand years old.</p>
    <p>There are many variations of passages available, but the majority have suffered alteration in some form, by injected humour or randomised words which don't look even slightly believable at all.</p>
  </div>
</section>

<section class="blog">
  <h2 class="section-title">LATEST FROM BLOG</h2>
  <div class="blog-row">
    <article class="post"><div class="shot" role="img" aria-label="Photo of a team discussing at a desk"><span class="date">25 MAY</span></div><div class="text"><h3>HEADING OF BLOG</h3><p>Lorem ipsum is simply dummy text of the printing and typesetting industry. It has been the standard dummy text ever since.</p><a>READ MORE</a></div></article>
    <article class="post"><div class="shot" role="img" aria-label="Photo of colleagues reviewing a laptop"><span class="date">25 MAY</span></div><div class="text"><h3>HEADING OF BLOG</h3><p>Lorem ipsum is simply dummy text of the printing and typesetting industry. It has been the standard dummy text ever since.</p><a>READ MORE</a></div></article>
  </div>
</section>

<section class="contact">
  <h2 class="section-title">CONTACT FORM</h2>
  <p class="sub">PLEASE FILL THE FORM BELOW, YOU COULD LEAVE US A MESSAGE</p>
  <div class="form">
    <div class="fields"><div class="field">NAME</div><div class="field">EMAIL</div><div class="field">PHONE</div></div>
    <div class="message">MESSAGE</div>
  </div>
  <span class="btn send">SEND MESSAGE</span>
</section>

<footer class="footer">
  <div class="col">
    <div class="brand"><span class="brand-dot"></span><span class="brand-name">Copper Wayfarer</span></div>
    <p>Digital Marketing, Elevated! Lorem ipsum dolor sit amet, consectetur adipiscing elit sed do eiusmod tempor.</p>
    <p style="margin-top:8px">Ut enim ad minim veniam, quis nostrud exercitation ullamco laboris nisi aliquip.</p>
  </div>
  <div class="col">
    <h4>FEATURED SERVICES</h4><div class="rule"></div>
    <ul><li>Website Design</li><li>Search Engine Optimization</li><li>Plexo Local Listing</li><li>Local Online Directories</li><li>Reputation Marketing</li><li>Social Media Marketing</li><li>Video Marketing</li><li>Pay Per Click</li></ul>
  </div>
  <div class="col">
    <h4>USEFUL LINKS</h4><div class="rule"></div>
    <ul><li>Home</li><li>About Us</li><li>Our Services</li><li>Blogs</li><li>Contact Us</li><li>Terms of Service</li><li>Privacy Policy</li></ul>
  </div>
  <div class="col">
    <h4>CONTACT INFO</h4><div class="rule"></div>
    <p>Copper Wayfarer – Digital Marketing<br>41872 Cobblewick Drive<br>Evergreen, CO 80439<br>303-547-9183<br>hello@copperwayfarer.example</p>
    <div class="socials" aria-label="Chatterly, Peepline, Plexo+, ReelHub"><span></span><span></span><span></span><span></span></div>
  </div>
</footer>
<div class="copyright">© 2016 Copper Wayfarer. All rights reserved.</div>
</body>
</html>
```